Velmoria - 3D medical animations and high end visual content

Our company creates high end visual content and animations for medical global companies.
Our website - www.velmoria-studio.example
We would like to have an amazing business card for our CEO that he can use in the following exhebitions he is going to attend.
It is very important that the design will be memorable and diffrent. It has to reflect our brand design (you can have it from our website)
We would like to transmit innovation, prestige, luxury, aesthetics.
The card has to be Double Sided

Target Market(s)

Marketing managers in medical global companys

Industry/Entity Type

It Company

Contact Information for Business Card

Requirements
Nice to have
• It is very important that the design will be memorable and diffrent. It has to reflect our brand design (you can have it from our website)

```html
<!DOCTYPE html>
<html lang="en">
<head>
<meta charset="utf-8">
<title>Velmoria – Business Card</title>
<link rel="stylesheet" href="https://fonts.googleapis.com/css2?family=Open+Sans:wght@400;600&display=swap">
<style>
  :root {
    --page-bg: #e6e4e2;
    --card-light: #f5f3f2;
    --card-dark: #1b1b1b;
    --accent: #2a9fc0;
    --ink: #1d1d1d;
    --rule: #2a2a2a;
    --white: #ffffff;
  }
  * { margin: 0; padding: 0; box-sizing: border-box; }
  html, body {
    width: 1200px;
    height: 900px;
    overflow: hidden;
    background: var(--page-bg);
    font-family: "Open Sans", Arial, sans-serif;
  }
  .canvas {
    position: relative;
    width: 1200px;
    height: 900px;
    display: flex;
    align-items: center;
    justify-content: center;
  }
  .business-card {
    width: 880px;
    height: 544px;
    display: flex;
    flex-direction: column;
    box-shadow: 0 18px 40px rgba(0,0,0,0.18);
  }
  .card-info {
    height: 290px;
    background: var(--card-light);
    position: relative;
  }
  .name-row {
    position: absolute;
    top: 88px;
    left: 0;
    right: 0;
    display: flex;
    align-items: center;
  }
  .name-row .rule {
    height: 2px;
    background: var(--rule);
  }
  .name-row .rule-left { width: 190px; }
  .name-row .rule-right { flex: 1; margin-right: 4px; }
  .person {
    display: flex;
    align-items: center;
    padding: 0 22px 0 18px;
    white-space: nowrap;
  }
  .person-name {
    color: var(--accent);
    font-weight: 600;
    font-size: 27px;
    letter-spacing: 0.5px;
  }
  .person-title {
    color: var(--ink);
    font-size: 22px;
    margin-left: 8px;
    padding-left: 8px;
    border-left: 2px solid var(--ink);
    line-height: 1.1;
  }
  .contact {
    position: absolute;
    top: 154px;
    left: 0;
    right: 0;
    text-align: center;
    font-size: 22px;
    line-height: 37px;
    color: var(--ink);
    padding-left: 60px;
  }
  .contact .label { color: var(--accent); }
  .contact .sep {
    display: inline-block;
    width: 2px;
    height: 26px;
    background: var(--ink);
    vertical-align: -5px;
    margin: 0 6px;
  }
  .card-brand {
    flex: 1;
    background: var(--card-dark);
    display: flex;
    align-items: center;
    justify-content: center;
  }
  .brand-name {
    color: var(--white);
    font-weight: 400;
    font-size: 72px;
    letter-spacing: 3px;
    text-transform: uppercase;
  }
</style>
</head>
<body>
  <main class="canvas">
    <section class="business-card">
      <div class="card-info">
        <div class="name-row">
          <span class="rule rule-left"></span>
          <div class="person">
            <span class="person-name">NOAM ADLER</span>
            <span class="person-title">FOUNDER &amp; CEO</span>
          </div>
          <span class="rule rule-right"></span>
        </div>
        <div class="contact">
          <p><span class="label">M:</span> +972-54-3107264<span class="sep"></span><span class="label">P:</span>&nbsp; +972-73-5520418</p>
          <p><span class="label">E:</span> noam@velmoria-studio.example<span class="sep"></span><span class="label">W:</span> www.velmoria-studio.example</p>
        </div>
      </div>
      <div class="card-brand">
        <span class="brand-name">Velmoria</span>
      </div>
    </section>
  </main>
</body>
</html>
```